Brindle Pet Shop Homepage

We are a pet shop, we focus on dog food / cat food / rodents & bird food

Based on WooCommerce

It should be a simple but professional homepage with an informative start page. In the shop it should then be possible to shop for products/manufacturers etc. Navigation/Filter menu on the left would be ideal.

Next menus:
ABOUT US
CONTACT
DOG
CAT
HOLDER

My Account - Login
My Cart

Footer:
Conditions
payment options
social media

In addition to our logo, I have attached 2 example pages from another shop which we would use as a guideline.

Target Market(s)

pet store

Industry/Entity Type

Animal, Pet Shop

Coding

Coded - Design and coding required

Number of Pages Required

1 page

Font styles to use
Sans Serif

Colors
0054AA
0677BA
7BADD7
CADEEF
E8F1F8

Requirements
Must have
• Main Page, Contact, About Us, Shop, Check Out, Member Login, Mailchimp Marketing - We work with WooCommerce

```html
<!DOCTYPE html>
<html lang="en">
<head>
<meta charset="utf-8">
<title>Brindle Pet Shop – Premium Pet Food</title>
<link href="https://fonts.googleapis.com/css2?family=Mulish:wght@400;600;700;800;900&display=swap" rel="stylesheet">
<style>
:root{
  --blue:#0054aa;
  --blue-mid:#0677ba;
  --blue-soft:#7badd7;
  --blue-pale:#cadeef;
  --blue-tint:#e8f1f8;
  --ink:#1d1d1f;
  --text:#444;
  --white:#fff;
  --line:#e3e7ec;
}
*{box-sizing:border-box;margin:0;padding:0}
html,body{width:1200px;height:3653px;overflow:hidden}
body{font-family:'Mulish',Arial,sans-serif;color:var(--ink);background:var(--white);position:relative}
.abs{position:absolute}
.btn{display:inline-flex;align-items:center;justify-content:center;background:var(--blue);color:var(--white);font-size:13px;font-weight:600;text-decoration:none}
.photo{position:absolute}

/* header */
.site-header{position:absolute;top:0;left:0;width:1200px;height:91px;background:var(--white)}
.brand{position:absolute;left:130px;top:22px;display:flex;align-items:center;gap:8px}
.brand-mark{width:34px;height:34px;border-radius:50%;background:var(--blue)}
.brand-text{display:flex;flex-direction:column;color:var(--blue);font-weight:800;font-size:17px;line-height:1}
.brand-text small{font-size:9px;font-weight:800;letter-spacing:1px;margin-top:4px}
.main-nav{position:absolute;left:395px;top:34px;display:flex;gap:36px;font-size:13px;font-weight:600;color:#333}
.main-nav a{color:inherit;text-decoration:none;padding-bottom:8px}
.main-nav a.active{color:var(--blue);font-weight:800;border-bottom:2px solid var(--blue)}
.cart-btn{position:absolute;left:888px;top:25px;width:98px;height:35px;border:1px solid var(--blue);display:flex;align-items:center;justify-content:center;gap:6px;font-size:12px;color:#333}
.login-btn{position:absolute;left:999px;top:25px;width:68px;height:34px;font-size:14px}

/* hero */
.hero{position:absolute;top:91px;left:0;width:1200px;height:516px;background:linear-gradient(90deg,#4e4638 0%,#6b5a40 40%,#8a5a2e 70%,#5a3a20 100%)}
.hero h1{position:absolute;left:133px;top:80px;font-size:68px;line-height:68px;font-weight:900;color:var(--white)}
.hero p{position:absolute;left:134px;top:239px;width:360px;font-size:19px;line-height:26px;color:var(--white)}
.hero .btn{position:absolute;left:135px;top:342px;width:127px;height:46px;font-size:16px;font-weight:500}
.dots{position:absolute;left:572px;top:470px;display:flex;gap:12px}
.dots span{width:11px;height:11px;border-radius:50%;background:var(--white)}
.dots span.on{background:var(--blue)}

/* categories */
.category{position:absolute;top:642px;width:304px;height:487px;background:var(--blue-tint);text-align:center}
.category .photo{left:0;top:0;width:304px;height:292px}
.category h3{position:absolute;top:318px;width:100%;font-size:16px;font-weight:800;color:var(--blue)}
.category p{position:absolute;top:350px;left:30px;width:244px;font-size:12px;line-height:17px;color:var(--text)}
.category .btn{position:absolute;top:422px;left:106px;width:91px;height:31px;font-size:12px}

/* welcome */
.welcome{position:absolute;top:1180px;left:0;width:1200px;height:531px}
.welcome .photo{left:0;top:0;width:766px;height:531px;background:linear-gradient(90deg,#a47656 0%,#c9c3bc 40%,#b7b4b0 70%,#d8d6d3 100%)}
.ring{position:absolute;left:564px;top:0;width:300px;height:531px;border-radius:265px 0 0 265px;background:rgba(255,255,255,.35)}
.welcome-circle{position:absolute;left:609px;top:35px;width:458px;height:458px;border-radius:50%;background:var(--blue);color:var(--white);text-align:center}
.welcome-circle h2{position:absolute;top:82px;width:100%;font-size:25px;line-height:31px;font-weight:900}
.welcome-circle .rule{position:absolute;top:166px;left:207px;width:32px;height:3px;background:var(--white)}
.welcome-circle p{position:absolute;top:188px;left:75px;width:310px;font-size:13px;line-height:19px}
.welcome-circle .btn{position:absolute;top:370px;left:179px;width:92px;height:31px;background:var(--white);color:var(--blue)}
.welcome svg{position:absolute;left:609px;top:35px}

/* section titles */
.section-title{position:absolute;width:1200px;left:0;text-align:center;font-size:28px;font-weight:900}
.section-title::after{content:"";display:block;width:32px;height:3px;background:var(--blue);margin:20px auto 0}

/* products */
.product{position:absolute;top:1857px;width:220px;height:390px;border:1px solid var(--line);text-align:center}
.product .photo{left:35px;top:30px;width:150px;height:150px;border-radius:6px}
.product h4{position:absolute;top:210px;width:100%;font-size:13px;font-weight:800}
.product p{position:absolute;top:238px;left:30px;width:160px;font-size:10.5px;line-height:15px;color:var(--text)}
.product .price{position:absolute;top:290px;width:100%;font-size:17px}
.product .btn{position:absolute;top:331px;left:66px;width:88px;height:29px;font-size:12px}
.arrow{position:absolute;top:2050px;width:31px;height:31px;border:1px solid #999;border-radius:50%;display:flex;align-items:center;justify-content:center}

/* bird */
.bird{position:absolute;top:2299px;left:0;width:1200px;height:505px;background:linear-gradient(90deg,#b6620f 0%,#e39a34 35%,#d48a2a 65%,#c7761c 100%)}
.bird-card{position:absolute;left:142px;top:94px;width:392px;height:323px;background:rgba(255,255,255,.92);padding:32px 42px}
.bird-card h2{font-size:28px;font-weight:900;margin-bottom:10px}
.bird-card p{font-size:12.3px;line-height:17.4px;color:#333}
.bird-card .btn{margin-top:16px;width:91px;height:31px}

/* guide */
.guide{position:absolute;top:2941px;width:296px}
.guide .photo{position:relative;display:block;width:296px;height:206px}
.guide h4{margin-top:25px;font-size:17px;line-height:22px;font-weight:600;color:#333}
.guide p{margin-top:18px;font-size:12px;line-height:17px;color:var(--text)}
.guide .btn{margin-top:20px;width:91px;height:31px}

/* footer */
.site-footer{position:absolute;top:3386px;left:0;width:1200px;height:267px;background:var(--blue);color:var(--white)}
.footer-brand{position:absolute;left:134px;top:46px;display:flex;align-items:center;gap:10px}
.footer-brand .brand-mark{width:52px;height:52px;background:var(--white)}
.footer-brand .brand-text{color:var(--white);font-size:22px}
.footer-brand .brand-text small{font-size:12px;letter-spacing:1.5px}
.f-label{position:absolute;top:82px;font-size:13px;font-weight:800}
.f-divider{position:absolute;top:36px;width:2px;height:98px;background:var(--white)}
.f-menu{position:absolute;left:464px;top:36px;list-style:none;font-size:11px;line-height:17.5px}
.f-contact{position:absolute;left:682px;top:40px;font-size:11.5px;line-height:16px}
.social{position:absolute;top:68px;width:27px;height:27px;border-radius:50%;background:var(--white)}
.f-rule{position:absolute;left:130px;top:180px;width:939px;height:1px;background:rgba(255,255,255,.35)}
.f-legal{position:absolute;left:130px;top:219px;font-size:11px}
.pay{position:absolute;top:215px;width:38px;height:24px;border-radius:3px;background:var(--blue-pale)}
</style>
</head>
<body>

<header class="site-header">
  <div class="brand"><span class="brand-mark"></span><span class="brand-text">BRINDLE PET<small>PREMIUM PET FOOD</small></span></div>
  <nav class="main-nav">
    <a class="active" href="#">HOME</a><a href="#">ABOUT US</a><a href="#">CONTACT</a><a href="#">DOG</a><a href="#">CAT</a><a href="#">HOLDER</a>
  </nav>
  <a class="cart-btn" href="#">
    <svg width="18" height="16" viewBox="0 0 18 16" fill="none" stroke="#333" stroke-width="1.4"><path d="M1 1h3l2 9h9l2-6H5"/><circle cx="7" cy="14" r="1.2"/><circle cx="14" cy="14" r="1.2"/></svg>
    My Cart</a>
  <a class="btn login-btn" href="#">Login</a>
</header>

<section class="hero" role="img" aria-label="Close-up photo of a brown dog in profile against a soft blurred background">
  <h1>PREMIUM<br>PET FOOD</h1>
  <p>Lorem ipsum dolor sit amet, consectetur adipiscing elit, sed do eiusmod tempor incididunt ut labore.</p>
  <a class="btn" href="#">Shop Now</a>
  <div class="dots"><span></span><span class="on"></span><span></span></div>
</section>

<article class="category" style="left:130px">
  <div class="photo" role="img" aria-label="Golden puppy holding a flower in its mouth" style="background:linear-gradient(160deg,#6f7a58,#b28a5c 60%,#8c6a4c)"></div>
  <h3>DOG FOOD</h3>
  <p>Lorem ipsum dolor sit amet, consectetur adipiscing elit, sed do eiusmod tem por incididunt ut labore.</p>
  <a class="btn" href="#">Read More</a>
</article>
<article class="category" style="left:448px">
  <div class="photo" role="img" aria-label="Tabby cat sitting on white stairs" style="background:linear-gradient(160deg,#d6d6d4,#a8998a 55%,#ecebe8)"></div>
  <h3>CAT FOOD</h3>
  <p>Lorem ipsum dolor sit amet, consectetur adipiscing elit, sed do eiusmod tem por incididunt ut labore.</p>
  <a class="btn" href="#">Read More</a>
</article>
<article class="category" style="left:766px">
  <div class="photo" role="img" aria-label="White hamster eating a food pellet" style="background:linear-gradient(160deg,#0f5f74,#d9d3c9 55%,#c58a2e)"></div>
  <h3>RODENTS FOOD</h3>
  <p>Lorem ipsum dolor sit amet, consectetur adipiscing elit, sed do eiusmod tem por incididunt ut labore.</p>
  <a class="btn" href="#">Read More</a>
</article>

<section class="welcome">
  <div class="photo" role="img" aria-label="A dog and a cat eating from metal bowls on a wooden floor"></div>
  <div class="ring"></div>
  <div class="welcome-circle">
    <h2>WELCOME TO<br>BRINDLE PET SHOP</h2>
    <span class="rule"></span>
    <p>Sed ut perspiciatis unde omnis iste natus error sit voluptatem accusantium doloremque laudantium, totam rem aperiam, eaque ipsa quae ab illo inventore veritatis et quasi architecto beatae vitae dicta sunt explicabo. Nemo enim ipsam voluptatem quia voluptas sit aspernatur aut odit aut fugit, sed quia consequuntur magni dolores eos.</p>
    <a class="btn" href="#">Read More</a>
  </div>
</section>

<h2 class="section-title" style="top:1757px">OUR PRODUCTS</h2>

<div class="arrow" style="left:64px"><svg width="10" height="14" viewBox="0 0 10 14" fill="none" stroke="#777" stroke-width="1.5"><path d="M7 1L2 7l5 6"/></svg></div>
<div class="arrow" style="left:1106px"><svg width="10" height="14" viewBox="0 0 10 14" fill="none" stroke="#777" stroke-width="1.5"><path d="M3 1l5 6-5 6"/></svg></div>

<article class="product" style="left:130px">
  <div class="photo" role="img" aria-label="Two bags of cat and dog food" style="background:linear-gradient(90deg,#2c8a7a,#9fb48f)"></div>
  <h4>Lorem ipsum dolor</h4>
  <p>Lorem ipsum dolor sit amet, consectetur adipiscing elit sed do eiusmod tem.</p>
  <div class="price">$25.99</div>
  <a class="btn" href="#">Add to cart</a>
</article>
<article class="product" style="left:369px">
  <div class="photo" role="img" aria-label="Clear bag of dry kibble" style="background:linear-gradient(180deg,#8c5a3a,#6a3d28)"></div>
  <h4>Lorem ipsum dolor</h4>
  <p>Lorem ipsum dolor sit amet, consectetur adipiscing elit sed do eiusmod tem.</p>
  <div class="price">$25.99</div>
  <a class="btn" href="#">Add to cart</a>
</article>
<article class="product" style="left:608px">
  <div class="photo" role="img" aria-label="Green and red bag of dog food" style="background:linear-gradient(180deg,#9ec22c,#c83b2a 55%,#9ec22c)"></div>
  <h4>Lorem ipsum dolor</h4>
  <p>Lorem ipsum dolor sit amet, consectetur adipiscing elit sed do eiusmod tem.</p>
  <div class="price">$25.99</div>
  <a class="btn" href="#">Add to cart</a>
</article>
<article class="product" style="left:850px">
  <div class="photo" role="img" aria-label="Red and white bag of dog food" style="background:linear-gradient(180deg,#e2403a,#f3f0ea 50%,#8cbc3a)"></div>
  <h4>Lorem ipsum dolor</h4>
  <p>Lorem ipsum dolor sit amet, consectetur adipiscing elit sed do eiusmod tem.</p>
  <div class="price">$25.99</div>
  <a class="btn" href="#">Add to cart</a>
</article>

<section class="bird" role="img" aria-label="Small yellow songbird in flight over a golden field of daisies">
  <div class="bird-card">
    <h2>BIRD FOOD</h2>
    <p>Sed ut perspiciatis unde omnis iste natus error sit voluptatem accusantium doloremque laudantium, totam rem aperiam, eaque ipsa quae ab illo inventore veritatis et quasi architecto beatae vitae dicta sunt explicabo. Nemo enim ipsam voluptatem quia voluptas sit aspernatur aut odit aut fugit, sed quia consequuntur magni dolores eos qui ratione voluptatem sequi nesciunt. Neque porro quisquam est, qui dolorem ipsum quia dolor</p>
    <a class="btn" href="#">Read More</a>
  </div>
</section>

<h2 class="section-title" style="top:2846px">ANIMAL GUIDE</h2>

<article class="guide" style="left:130px">
  <div class="photo" role="img" aria-label="Golden dog and grey cat sharing a food bowl" style="background:linear-gradient(90deg,#b9763c,#e8e4de 60%,#8a8580)"></div>
  <h4>Lorem ipsum dolor sit amet consectetur adipiscing</h4>
  <p>Sed ut perspiciatis unde omnis iste natus error sit voluptatem accusantium doloremque laudantium, totam rem aperiam, eaque ipsa quae ab illo inventore veritatis</p>
  <a class="btn" href="#">Read More</a>
</article>
<article class="guide" style="left:451px">
  <div class="photo" role="img" aria-label="Groundhog peeking out of snow" style="background:linear-gradient(180deg,#8a97a6,#e9ecef 45%,#8c6a48 75%,#f0f2f4)"></div>
  <h4>Lorem ipsum dolor sit amet consectetur adipiscing</h4>
  <p>Sed ut perspiciatis unde omnis iste natus error sit voluptatem accusantium doloremque laudantium, totam rem aperiam, eaque ipsa quae ab illo inventore veritatis</p>
  <a class="btn" href="#">Read More</a>
</article>
<article class="guide" style="left:772px">
  <div class="photo" role="img" aria-label="Blue bird perched on a branch" style="background:linear-gradient(135deg,#6a7060,#3a4a8a 50%,#4e5a48)"></div>
  <h4>Lorem ipsum dolor sit amet consectetur adipiscing</h4>
  <p>Sed ut perspiciatis unde omnis iste natus error sit voluptatem accusantium doloremque laudantium, totam rem aperiam, eaque ipsa quae ab illo inventore veritatis</p>
  <a class="btn" href="#">Read More</a>
</article>

<footer class="site-footer">
  <div class="footer-brand"><span class="brand-mark"></span><span class="brand-text">BRINDLE PET<small>PREMIUM PET FOOD</small></span></div>
  <span class="f-label" style="left:373px">MENU</span>
  <span class="f-divider" style="left:436px"></span>
  <ul class="f-menu"><li>HOME</li><li>ABOUT US</li><li>CONTACT</li><li>DOG</li><li>CAT</li><li>HOLDER</li></ul>
  <span class="f-label" style="left:578px">CONTACT</span>
  <span class="f-divider" style="left:659px"></span>
  <div class="f-contact">41 Maplewood Ave, Kelton,<br>ON K2B 4R8, Canada<br><br style="line-height:8px">+1 555 014 2290<br><br style="line-height:8px">info@brindlepetshop.com</div>
  <span class="f-label" style="left:879px">FOLLOW</span>
  <span class="f-divider" style="left:951px"></span>
  <span class="social" style="left:964px"></span>
  <span class="social" style="left:1002px"></span>
  <span class="social" style="left:1040px"></span>
  <span class="f-rule"></span>
  <div class="f-legal">Conditions &nbsp; | &nbsp; Copyright © 2023 All Rights Reserved</div>
  <span class="pay" style="left:902px"></span>
  <span class="pay" style="left:945px"></span>
  <span class="pay" style="left:988px"></span>
  <span class="pay" style="left:1031px"></span>
</footer>

</body>
</html>
```